I have a logo and need to design the business card and stationery.
Updates

The uploaded logo image named as GREYHAVEN CONSTRUCTION which is to be replaced to GREYHAVEN CONTRACTS. Kindly add below details and submit the designs- Company name- Greyhaven Engineering Contracts LLP Name & Post- Kunal Mehra (Designated Partner) Address- Block No.317, Wing C, Tulsi Trade Plaza, Lokhand Marg, Varun Industrial Park, Goregaon(E), Mumbai - 400 063 Contact- +91 97410 58723 Email- kunalmehra@examplemail.com Website- www.greyhavencontracts.example Contact for Letterhead- +91-22-28145597

Hi Tanvir Rahman, We are liking your Design #41927506. We have suggested some changes which are mentioned in feedback. Kindly revert with it asap to finalize this design.

Colors

Designer to choose colors to be used in the design.

```html
<!DOCTYPE html>
<html lang="en">
<head>
<meta charset="utf-8">
<title>Greyhaven Contracts — Business Card</title>
<link href="https://fonts.googleapis.com/css2?family=Oswald:wght@500&family=Montserrat:wght@400;600&family=Roboto:wght@400&display=swap" rel="stylesheet">
<style>
  :root {
    --backdrop: #4a4a4a;
    --card-front: #ffffff;
    --card-back: #323232;
    --ink: #2b2b2b;
    --ink-soft: #3a3a3a;
    --mark-fill: #1f1f1f;
    --brand-text: #bdbdbd;
    --tagline: #ffffff;
  }
  * { margin: 0; padding: 0; box-sizing: border-box; }
  html, body {
    width: 1135px;
    height: 1200px;
    overflow: hidden;
    background: var(--backdrop);
  }
  .canvas {
    position: relative;
    width: 1135px;
    height: 1200px;
  }
  .card {
    position: absolute;
    left: 205px;
    width: 726px;
    height: 415px;
  }
  .card--front { top: 145px; background: var(--card-front); }
  .card--back  { top: 641px; background: var(--card-back); }

  .identity {
    position: absolute;
    right: calc(726px - 305px);
    top: 180px;
    text-align: right;
  }
  .identity__name {
    font-family: 'Oswald', sans-serif;
    font-weight: 500;
    font-size: 46px;
    line-height: 1;
    letter-spacing: 1.5px;
    color: var(--ink);
    white-space: nowrap;
  }
  .identity__role {
    margin-top: 5px;
    font-family: 'Montserrat', sans-serif;
    font-weight: 400;
    font-size: 17px;
    letter-spacing: 1px;
    color: var(--ink-soft);
    white-space: nowrap;
  }
  .divider {
    position: absolute;
    left: 330px;
    top: 142px;
    width: 2px;
    height: 135px;
    background: var(--ink-soft);
  }
  .contact {
    position: absolute;
    left: 359px;
    top: 137px;
    font-family: 'Roboto', sans-serif;
    color: var(--ink);
  }
  .contact__address {
    font-size: 16.5px;
    line-height: 22.5px;
    letter-spacing: 0.6px;
    font-style: normal;
    white-space: nowrap;
  }
  .contact__list {
    list-style: none;
    margin-top: 5px;
  }
  .contact__item {
    display: flex;
    align-items: center;
    gap: 6px;
    font-size: 18px;
    line-height: 24.5px;
    letter-spacing: 0.3px;
    white-space: nowrap;
  }
  .contact__icon { width: 13px; height: 13px; flex: none; }

  .brand {
    position: absolute;
    left: 0;
    right: 0;
    top: 107px;
    display: flex;
    flex-direction: column;
    align-items: center;
  }
  .brand__square {
    width: 123px;
    height: 122px;
    background: var(--mark-fill);
  }
  .brand__name {
    margin-top: 20px;
    font-family: 'Montserrat', sans-serif;
    font-weight: 600;
    color: var(--brand-text);
    text-align: center;
    white-space: nowrap;
  }
  .brand__line {
    display: block;
    line-height: 1;
  }
  .brand__line--main {
    font-size: 38px;
    letter-spacing: 14px;
    margin-right: -14px;
  }
  .brand__line--sub {
    margin-top: 9px;
    font-size: 21px;
    letter-spacing: 31px;
    margin-right: -31px;
  }
  .tagline {
    position: absolute;
    left: 0;
    right: 0;
    top: 357px;
    text-align: center;
    font-family: 'Montserrat', sans-serif;
    font-weight: 600;
    font-size: 17.5px;
    letter-spacing: 1px;
    color: var(--tagline);
  }
</style>
</head>
<body>
<main class="canvas">
  <section class="card card--front">
    <div class="identity">
      <h1 class="identity__name">KUNAL MEHRA</h1>
      <p class="identity__role">DESIGNATED PARTNER</p>
    </div>
    <div class="divider"></div>
    <div class="contact">
      <address class="contact__address">
        Block No.317, Wing C,<br>
        Tulsi Trade Plaza, Lokhand Marg,<br>
        Varun Industrial Park, Goregaon(E),<br>
        Mumbai - 400 063
      </address>
      <ul class="contact__list">
        <li class="contact__item">
          <svg class="contact__icon" viewBox="0 0 14 14" aria-hidden="true">
            <rect x="1" y="3" width="12" height="8.5" fill="none" stroke="#2b2b2b" stroke-width="1.2"/>
            <path d="M1 3.5 L7 8 L13 3.5" fill="none" stroke="#2b2b2b" stroke-width="1.2"/>
          </svg>
          info@greyhavencontracts.example
        </li>
        <li class="contact__item">
          <svg class="contact__icon" viewBox="0 0 14 14" aria-hidden="true">
            <circle cx="7" cy="7" r="5.8" fill="none" stroke="#2b2b2b" stroke-width="1"/>
            <ellipse cx="7" cy="7" rx="2.6" ry="5.8" fill="none" stroke="#2b2b2b" stroke-width="1"/>
            <path d="M1.2 7 H12.8 M2 4 H12 M2 10 H12" stroke="#2b2b2b" stroke-width="0.9"/>
          </svg>
          www.greyhavencontracts.example
        </li>
      </ul>
    </div>
  </section>

  <section class="card card--back">
    <div class="brand">
      <div class="brand__square"></div>
      <p class="brand__name">
        <span class="brand__line brand__line--main">GREYHAVEN</span>
        <span class="brand__line brand__line--sub">CONTRACTS</span>
      </p>
    </div>
    <p class="tagline">BUILT ON SOLID GROUND.</p>
  </section>
</main>
</body>
</html>
```